CD-/Plattencover für eine Tonträgerfirma
Zielgruppe
Wir sind eine Tonträgerfirma und bewegen uns im Low-Budget-Segment.
Aufgabenstellung
'Harbor Lanterns'
Wir benötigen nicht das komplette Artwork, sondern ein Frontcover
(121 x 120 mm + 20 mm Beschnitt) wg. etwaiger Verschiebung der Positionierung.
Fertigstellung (Aufziehen des Inlays und Labels) erfolgt später bei uns im Hause.
Wir benötigen später eine offene psd-Datei mit allen Ebenen.
Wichtig: Schriften nicht gerastert ggfs. Schrift mitliefern.
Was wir uns vorstellen:
- Entsprechend der Musik Bild
- Da es ein 2-CD-Set ist, sollte '2 CDs' auch gut auf dem Cover ersichtlich sein
- Folgende Titel sollten auf dem Cover genannt werden
Rowan Lad
Hills of Fern
Gentle Harrow
- Bildmaterial sollte bei pixelbarn, bildora oder n-pics ausgesucht werden,
das Bildmaterial wird dann später auch von uns dort eingekauft
- keine Künstlerfotos
- vorzugsweise nur 1 Bild pro Layout, max. 2 Bilder
Wir freuen uns und sind sehr gespannt auf eure Vorschläge,
bei Fragen gerne mailen

```html
<!DOCTYPE html>
<html lang="de">
<head>
<meta charset="utf-8">
<title>Harbor Lanterns – Frontcover</title>
<link rel="stylesheet" href="https://fonts.googleapis.com/css2?family=Uncial+Antiqua&display=swap">
<style>
  :root {
    --backdrop: #2a2b2d;
    --cover-edge: #f4f6f0;
    --meadow-light: #9fe04a;
    --meadow-mid: #5fbf2a;
    --meadow-deep: #2f7e1c;
    --sun-glow: #f3ea9c;
    --gold-light: #f6ecaa;
    --title-green: #3fd04a;
    --title-light: #b9f5a8;
    --title-dark: #0f5a1c;
    --caption: #f5f3e2;
  }
  html, body {
    margin: 0;
    width: 1200px;
    height: 829px;
    overflow: hidden;
    background: var(--backdrop);
  }
  .canvas {
    position: relative;
    width: 1200px;
    height: 829px;
  }
  .cover {
    position: absolute;
    left: 220px;
    top: 34px;
    width: 760px;
    height: 760px;
    box-sizing: border-box;
    border: 9px solid var(--cover-edge);
    overflow: hidden;
    font-family: "Uncial Antiqua", "Georgia", serif;
  }
  .cover-photo {
    position: absolute;
    inset: 0;
    background:
      radial-gradient(circle at 8% 6%, var(--sun-glow) 0%, rgba(243,234,156,0.55) 14%, rgba(243,234,156,0) 34%),
      linear-gradient(160deg, var(--meadow-light) 0%, var(--meadow-mid) 45%, var(--meadow-deep) 100%);
  }
  .emblem {
    position: absolute;
    left: 146px;
    top: 40px;
    width: 450px;
    height: 450px;
  }
  .title {
    position: absolute;
    left: 163px;
    width: 416px;
    top: 172px;
    margin: 0;
    text-align: center;
    font-weight: 400;
    font-size: 52px;
    line-height: 1.15;
    text-transform: uppercase;
    color: var(--title-green);
    text-shadow:
      -1px -1px 0 var(--title-light),
      2px 2px 0 var(--title-dark),
      3px 4px 6px rgba(0,0,0,0.35);
  }
  .title-line { display: block; white-space: nowrap; }
  .title-line--first { transform: translateX(-28px); }
  .title-line--second { transform: translateX(22px); }
  .edition {
    position: absolute;
    left: 146px;
    width: 450px;
    top: 392px;
    margin: 0;
    text-align: center;
    font-size: 20px;
    color: var(--gold-light);
    letter-spacing: 1px;
  }
  .tracklist {
    position: absolute;
    left: 0;
    right: 0;
    bottom: 34px;
    margin: 0;
    padding: 0 60px;
    list-style: none;
    display: flex;
    justify-content: space-between;
    font-size: 19px;
    color: var(--caption);
    text-shadow: 0 1px 3px rgba(0,0,0,0.35);
  }
</style>
</head>
<body>
<main class="canvas">
  <section class="cover">
    <div class="cover-photo" role="img" aria-label="Foto: sonnige grüne Hügellandschaft mit Gras und Steinen"></div>

    <svg class="emblem" viewBox="0 0 450 450" aria-hidden="true">
      <defs>
        <radialGradient id="emblemFill" cx="45%" cy="40%" r="60%">
          <stop offset="0%" stop-color="#2a8060"/>
          <stop offset="100%" stop-color="#14513a"/>
        </radialGradient>
        <linearGradient id="goldRing" x1="0" y1="0" x2="1" y2="1">
          <stop offset="0%" stop-color="#f6ecaa"/>
          <stop offset="50%" stop-color="#d9c46a"/>
          <stop offset="100%" stop-color="#f3e7a2"/>
        </linearGradient>
      </defs>
      <circle cx="225" cy="225" r="208" fill="url(#emblemFill)"/>
      <circle cx="225" cy="225" r="208" fill="none" stroke="url(#goldRing)" stroke-width="14"/>
    </svg>

    <h1 class="title">
      <span class="title-line title-line--first">Harbor</span>
      <span class="title-line title-line--second">Lanterns</span>
    </h1>
    <p class="edition">· 2 Disc Collection ·</p>

    <ul class="tracklist">
      <li>Rowan Lad</li>
      <li>Gentle Harrow</li>
      <li>Hills of Fern</li>
    </ul>
  </section>
</main>
</body>
</html>
```